Modern, pro female massage business needs business card design

We are a boutique, pro women's sports and remedial massage studio based in Singapore - we have a logo already (see attached image) and need to design a business card that reflects an elegant, modern and feminine feel using this logo.

We are focussed on a very local market and need to give a professional yet warm feeling.

Details for the card include (layout of your choice):

Tamsin Vale
Call, SMS or WhatsApp: 9183 6027
Email: bluefennel@mailbox-example.com
Address: The Harbourview on Talbot
72 Talbot Road, Westmere, Singapore

To incorporate the QRAB logo (www.qrabglobal.co.uk) would be appreciated - see attached file.

Industry/Entity Type

Massage

Requirements
Nice to have
• We like the idea of using an embossed style card. Solid colour on the reverse - embossed on the front; four colour printing is okay.
Should not have
• It should not be uber 'girly girl' if that makes any sense. The logo is already colourful

```html
<!DOCTYPE html>
<html lang="en">
<head>
<meta charset="utf-8">
<title>bluefennel – business card</title>
<link href="https://fonts.googleapis.com/css2?family=Open+Sans:wght@400;600;700;800&display=swap" rel="stylesheet">
<style>
  :root{
    --backdrop:#1c1c1c;
    --pink-deep:#dc1a83;
    --pink:#e6398f;
    --pink-light:#ee5ea3;
    --paper:#f0eeec;
    --paper-shade:#e6e3e0;
    --ink-brand:#9c2f63;
    --white:#ffffff;
    --badge:#2f6fb5;
  }
  *{margin:0;padding:0;box-sizing:border-box}
  html,body{width:1200px;height:716px;overflow:hidden;background:var(--backdrop)}
  body{font-family:"Open Sans",Arial,sans-serif;position:relative}
  .card{position:absolute;top:190px;width:520px;height:337px;overflow:hidden;box-shadow:0 10px 30px rgba(0,0,0,.45)}
  .card--front{left:60px}
  .card--back{left:620px}
  .card__fill{position:absolute;top:0;bottom:0}
  .card--front .card__fill{left:0;right:0;background:linear-gradient(135deg,var(--pink-deep) 0%,var(--pink) 55%,var(--pink-light) 100%)}
  .card__fill--paper{left:0;width:275px;background:linear-gradient(160deg,var(--paper) 0%,var(--paper-shade) 100%)}
  .card__fill--pink{left:275px;right:0;background:linear-gradient(135deg,var(--pink-deep) 0%,var(--pink) 60%,var(--pink-light) 100%)}
  .card__pointer{position:absolute;left:275px;top:160px;width:0;height:0;border-top:8px solid transparent;border-bottom:8px solid transparent;border-left:10px solid var(--paper-shade)}
  .brand{position:absolute;font-family:"Open Sans",Arial,sans-serif;line-height:1}
  .brand__name{font-weight:800;letter-spacing:-1.5px}
  .brand__tagline{font-weight:800;letter-spacing:-0.4px;margin-top:2px}
  .card--front .brand{left:132px;top:112px;color:var(--white)}
  .card--front .brand__name{font-size:46px}
  .card--front .brand__tagline{font-size:14px}
  .card--back .brand{left:22px;top:146px;color:var(--ink-brand)}
  .card--back .brand__name{font-size:34px}
  .card--back .brand__tagline{font-size:10.5px}
  .partner-badge{position:absolute;left:226px;top:178px;width:22px;height:26px;background:var(--badge);border-radius:2px}
  .contact{position:absolute;left:300px;top:110px;color:var(--white)}
  .contact__name{font-size:21px;font-weight:700;letter-spacing:.3px}
  .contact__line{display:flex;font-size:8.5px;line-height:1.45;margin-top:4px}
  .contact__call{font-weight:700;font-size:9px;margin-top:6px;display:flex;gap:20px}
  .contact__call .num{font-weight:400}
  .contact__key{width:12px;font-weight:700}
</style>
</head>
<body>

<section class="card card--front" aria-label="Card front">
  <div class="card__fill" role="img" aria-label="Pink background with soft curved swoosh pattern"></div>
  <div class="brand">
    <div class="brand__name">bluefennel</div>
    <div class="brand__tagline">Remedial and sports massage</div>
  </div>
</section>

<section class="card card--back" aria-label="Card back">
  <div class="card__fill card__fill--paper" role="img" aria-label="Off-white panel with faint curved swoosh pattern"></div>
  <div class="card__fill card__fill--pink" role="img" aria-label="Pink panel with soft curved swoosh pattern"></div>
  <div class="card__pointer"></div>
  <div class="brand">
    <div class="brand__name">bluefennel</div>
    <div class="brand__tagline">Remedial and sports massage</div>
  </div>
  <div class="partner-badge" aria-label="Partner badge"></div>
  <div class="contact">
    <div class="contact__name">Tamsin Vale</div>
    <div class="contact__call"><span>Call, sms , WhatsApp</span><span class="num">9183 6027</span></div>
    <div class="contact__line"><span class="contact__key">E</span><span>bluefennel@mailbox-example.com</span></div>
    <div class="contact__line"><span class="contact__key">A</span><span>The Harbourview on Talbot<br>72 Talbot Road, Westmere, Singapore</span></div>
  </div>
</section>

</body>
</html>
```